Business card design needed

I need a business card design for a dog walking, dog minding and dog training business. Please refer to my website for the basic company colours and fonts I'm after. Planning on a double sided card, so all information doesn't need to be on the 'front' side.
Cheers

Industry/Entity Type

Dog Training

Contact Information for Business Card

Meadow Paws - happy hounds
Rua 0498307164
meadowpawsdemo.com.au
-walking
-holiday stays
-onsite care
-training and behavioural consultations

```html
<!DOCTYPE html>
<html lang="en">
<head>
<meta charset="utf-8">
<title>Meadow Paws – Business Card</title>
<link rel="stylesheet" href="https://fonts.googleapis.com/css2?family=Roboto+Condensed:wght@400;700&display=swap">
<style>
  :root {
    --page: #ffffff;
    --page-edge: #c9c9c9;
    --card-face: #dcdcdc;
    --card-edge: #9a9a9a;
    --ink-grey: #58595b;
    --dot-grey: #a8a8a8;
    --band-grey: #a9a7a3;
    --brand-orange: #e85a13;
    --brand-blue: #20288a;
    --slate: #636365;
    --white: #ffffff;
  }
  * { box-sizing: border-box; margin: 0; padding: 0; }
  html, body { width: 1200px; height: 1000px; overflow: hidden; background: var(--page); }
  body { font-family: "Roboto Condensed", "Arial Narrow", sans-serif; position: relative; }
  .canvas { position: absolute; inset: 0; border: 1px solid var(--page-edge); }
  .card {
    position: absolute; left: 99px; top: 210px; width: 1006px; height: 580px;
    background: var(--white); border: 1px solid var(--card-edge); overflow: hidden;
  }
  .card__face { position: absolute; left: 0; top: 0; width: 100%; height: 376px; background: var(--card-face); }
  .card__url {
    position: absolute; left: 143px; top: 180px; font-size: 31px; color: var(--ink-grey);
    letter-spacing: 0.2px;
  }
  .card__dots { position: absolute; left: 10px; top: 221px; }
  .brand { position: absolute; left: 572px; top: 168px; display: flex; align-items: center; gap: 16px; }
  .brand__dot { width: 54px; height: 54px; border-radius: 50%; background: var(--brand-orange); }
  .brand__text { display: flex; flex-direction: column; }
  .brand__name { font-size: 36px; font-weight: 700; color: var(--brand-orange); line-height: 1; letter-spacing: 0.5px; }
  .brand__tagline { font-size: 21px; color: var(--ink-grey); line-height: 1.1; margin-top: 2px; }
  .services {
    position: absolute; left: 0; top: 376px; width: 100%; height: 51px; background: var(--band-grey);
    color: var(--white); font-size: 31px; display: flex; align-items: center; justify-content: center;
    letter-spacing: 0.2px;
  }
  .tiles { position: absolute; left: 0; top: 437px; width: 100%; height: 143px; }
  .tile { position: absolute; top: 0; height: 143px; }
  .tile--blue { left: 0; width: 329px; background: var(--brand-blue); }
  .tile--orange { left: 337px; width: 329px; background: var(--brand-orange); display: flex; align-items: center; padding-left: 18px; gap: 20px; }
  .tile--slate { left: 677px; width: 329px; background: var(--slate); }
  .contact__number { color: var(--white); font-size: 32px; letter-spacing: 0.3px; }
</style>
</head>
<body>
<div class="canvas">
  <div class="card">
    <div class="card__face">
      <div class="card__url">http://meadowpawsdemo.com.au</div>
      <svg class="card__dots" width="550" height="12" viewBox="0 0 550 12" aria-hidden="true">
        <defs>
          <pattern id="dotRow" width="13.2" height="12" patternUnits="userSpaceOnUse">
            <circle cx="5" cy="6" r="4.6" fill="var(--dot-grey)"/>
          </pattern>
        </defs>
        <rect width="550" height="12" fill="url(#dotRow)"/>
      </svg>
      <div class="brand">
        <div class="brand__dot"></div>
        <div class="brand__text">
          <span class="brand__name">MEADOW PAWS</span>
          <span class="brand__tagline">happy hounds</span>
        </div>
      </div>
    </div>
    <div class="services">walking - holiday stays - onsite care - training and behavioural consultations</div>
    <div class="tiles">
      <div class="tile tile--blue"></div>
      <div class="tile tile--orange">
        <svg class="contact__icon" width="44" height="30" viewBox="0 0 44 30" aria-label="Phone">
          <path d="M2 8 Q22 -2 42 8 L40 13 L31 12 L30 8 Q22 6 14 8 L13 12 L4 13 Z" fill="var(--white)"/>
          <path d="M10 14 L34 14 L38 29 L6 29 Z" fill="var(--white)"/>
          <circle cx="22" cy="21" r="5.5" fill="var(--brand-orange)"/>
          <circle cx="22" cy="21" r="2.5" fill="var(--white)"/>
        </svg>
        <span class="contact__number">Rua 0498 307 164</span>
      </div>
      <div class="tile tile--slate"></div>
    </div>
  </div>
</div>
</body>
</html>
```